Online-Marketing Material für Beraternetzwerk
Zielgruppe
Ich habe ein Beraternetzwerk im deutschen Gesundheitswesen gegründet, gleichzeitig einen gemeinnützigen Verein, habe zwei webseiten www.kv-pflegeberatung-demo.de + www.kv-pflegefreunde-demo.de, Logo, Briefpapier etc. sind vorhanden. Hauptfarbe GmbH RGB 185/87/120 Hex#B95778, Verein RGB 226/125/119 Hex#E27D77. Die Organisationen sind grundsätzlich getrennt, aber es gibt eine Zusammenarbeit und Partner meines Netzwerkes sind auch Fördermitglieder im Verein
Aufgabenstellung
Die beiden Firmenfarben müssen verwendet werden, für die GmbH hauptsächlich die eigene, die 2. Farbe darf mit verwendet werden. Es darf insgesamt feminin wirken, aber nicht verspielt oder gar niedlich. Ich bin Business-Frau;-). Als Schrift habe ich mich auf Avenir next konzentriert, die Agentur hat auch Alternate Gothic auf den Webseiten verwendet. Jetzt benötige ich für eine Veranstaltungsreihe die Ausarbeitung von LinkedIn, Facebook/Insta, Einladung per Brevo und E-Mail Grafiken. Es sind immer Veranstaltungen, zu denen ich einlade und in denen meine Geschäftspartner ihre Expertise gegenüber Kunden darstellen. Die Veranstaltungen sind als Duo zu sehen 1. Präsenz in München, 2. als Online Meeting ein paar Tage später. Die Location wird das Hotel Marwin, direkt am Brunnenhofplatz in München sein. Start der Präsenzveranstaltung 11:00, anschließend Mittagessen. Als Titel für die Veranstaltungen sehe ich 'KlinikForum' vor, es wird jeweils noch ein inhaltliches Thema wie z.B. 'Unternehmenskauf/-verkauf' ergänzt. Erster Termin ist vss. am 15. September 2023. Anbei auch ein paar erste Entwürfe 'meiner' Agentur nebst Feedback von mir. Ich glaube inzwischen nicht, dass hier etwas vernünftiges produziert wird, deshalb mein Versuch auf diesem Weg. Weitere Zusammenarbeit dann herzlich gerne

```html
<!DOCTYPE html>
<html lang="de">
<head>
<meta charset="utf-8">
<title>KlinikForum – Unternehmenskauf/-verkauf</title>
<link rel="stylesheet" href="https://fonts.googleapis.com/css2?family=Nunito+Sans:wght@300;400;600;700;800;900&display=swap">
<style>
  :root {
    --brand: #B95778;
    --brand-bright: #c95b87;
    --brand-deep: #9e4466;
    --brand-text: #a24a6d;
    --blush: #e7a3bd;
    --paper: #ffffff;
    --stone-light: #e9e2d6;
    --stone: #d8cdbd;
    --stone-dark: #bfb3a3;
    --suit: #4a4d55;
  }
  * { margin: 0; padding: 0; box-sizing: border-box; }
  html, body {
    width: 1200px; height: 630px; overflow: hidden;
    background: var(--paper);
  }
  .event-card {
    position: relative; width: 1200px; height: 630px; overflow: hidden;
    font-family: "Nunito Sans", sans-serif;
    color: var(--brand);
    background: var(--paper);
  }
  .portrait {
    position: absolute; left: 0; top: 0; width: 600px; height: 630px;
    background:
      radial-gradient(ellipse 170px 300px at 240px 360px, var(--suit) 0%, var(--suit) 55%, transparent 75%),
      linear-gradient(135deg, var(--stone-light) 0%, var(--stone) 55%, var(--stone-dark) 100%);
  }
  .tint {
    position: absolute; inset: 0;
    background:
      linear-gradient(to bottom, transparent 0%, transparent 55%, rgba(255,255,255,0.85) 100%),
      linear-gradient(to right, transparent 0%, transparent 30%, rgba(222,140,172,0.75) 48%, var(--blush) 100%);
  }
  .fade-bottom {
    position: absolute; left: 0; right: 0; bottom: 0; height: 330px;
    background: linear-gradient(to bottom, rgba(255,255,255,0) 0%, rgba(255,255,255,0.9) 70%, #fff 100%);
  }
  .headline {
    position: absolute; left: 342px; top: 22px; width: 815px;
    display: flex; justify-content: space-between;
    font-size: 112px; line-height: 1; letter-spacing: 1px;
    color: var(--brand-bright);
    text-transform: uppercase;
  }
  .headline-light { font-weight: 300; }
  .headline-bold { font-weight: 900; }
  .programme {
    position: absolute; left: 470px; top: 176px; width: 420px;
    text-align: center; color: var(--brand-text);
  }
  .topic { font-size: 25px; font-weight: 800; line-height: 1.2; }
  .format { margin-top: 20px; font-size: 37px; font-weight: 800; line-height: 1; }
  .start-time { margin-top: 2px; font-size: 78px; font-weight: 900; line-height: 1; }
  .venue { margin-top: 2px; font-size: 23px; font-weight: 800; }
  .venue-note { font-size: 19px; font-weight: 400; color: var(--brand); }
  .online-band {
    position: absolute; left: 486px; top: 420px; width: 384px; height: 38px;
  }
  .online-band svg { position: absolute; inset: 0; }
  .online-band span {
    position: relative; display: block; text-align: center;
    line-height: 38px; font-size: 18px; font-weight: 400; color: var(--paper);
  }
  .date-flag { position: absolute; left: 922px; top: 186px; width: 238px; height: 350px; }
  .date-flag svg { position: absolute; inset: 0; }
  .date-text {
    position: relative; text-align: center; color: var(--paper);
    padding-top: 48px;
  }
  .date-day { font-size: 108px; font-weight: 900; line-height: 0.95; }
  .date-month { font-size: 40px; font-weight: 400; line-height: 1.15; }
  .date-year { font-size: 76px; font-weight: 900; line-height: 0.95; }
  .brand {
    position: absolute; left: 452px; top: 516px;
    display: flex; align-items: center; gap: 18px;
  }
  .brand-dot { width: 64px; height: 64px; border-radius: 50%; background: var(--brand); }
  .brand-name {
    font-size: 32px; font-weight: 700; line-height: 1.12; color: var(--brand);
  }
  .registration {
    position: absolute; left: 920px; top: 544px; width: 280px;
    text-align: center; color: var(--brand);
  }
  .registration-note { font-size: 11px; line-height: 1.3; }
  .registration-note strong { font-weight: 800; }
  .registration-mail { margin-top: 14px; font-size: 15px; }
</style>
</head>
<body>
<main class="event-card">
  <div class="portrait" role="img" aria-label="Porträtfoto der Gastgeberin im grauen Blazer vor einer hellen Steinwand"></div>
  <div class="tint"></div>
  <div class="fade-bottom"></div>

  <h1 class="headline">
    <span class="headline-light">Klinik</span><span class="headline-bold">Forum</span>
  </h1>

  <section class="programme">
    <p class="topic">“Unternehmenskauf/-verkauf”</p>
    <p class="format">Präsenzveranstaltung</p>
    <p class="start-time">11:00</p>
    <p class="venue">im Hotel Marwin</p>
    <p class="venue-note">direkt am Brunnenhofplatz</p>
  </section>

  <div class="online-band">
    <svg width="384" height="38" viewBox="0 0 384 38" aria-hidden="true">
      <polygon points="14,0 384,0 370,38 0,38" fill="var(--brand-deep)"/>
    </svg>
    <span>Online am x.xx. 17:00</span>
  </div>

  <div class="date-flag">
    <svg width="238" height="350" viewBox="0 0 238 350" aria-hidden="true">
      <polygon points="0,46 238,0 238,302 0,348" fill="var(--brand-bright)"/>
    </svg>
    <div class="date-text">
      <p class="date-day">15.</p>
      <p class="date-month">September</p>
      <p class="date-year">2023</p>
    </div>
  </div>

  <div class="brand">
    <span class="brand-dot"></span>
    <p class="brand-name">KV Pflegeberatung<br>GmbH</p>
  </div>

  <aside class="registration">
    <p class="registration-note">Begrenze Teilnehmerzahl<br><strong>Bitte anmelden unter:</strong></p>
    <p class="registration-mail">info@kv-pflegeberatung-demo.de</p>
  </aside>
</main>
</body>
</html>
```